Need effective Landing Page for product and service

Need help re-designing landing page:

Our company (in New York) offers upgrades to homes to make them more efficient, save energy and reduce utility bills. We do not do, or suggest every possible measure, like sealing and insulating a home, replacing windows, etc. We only offer high efficiency Ductless Mini Split Systems.

The landing page is to introduce the idea, and get people to fill the form. We already running a page at www.breezlotech.net, but it is dull and boring, while it must be exciting, creating an urge to fill the form (schedule live consultation).

Visitors get to the page from Facebook Ad, designer must make sure there is congruence between the ad and the page.

Industry/Entity Type

Product

```html
<!DOCTYPE html>
<html lang="en">
<head>
<meta charset="utf-8">
<title>Aerolume – Ductless Heat and Cool Consultation</title>
<link href="https://fonts.googleapis.com/css2?family=Open+Sans:wght@300;400;600;700&display=swap" rel="stylesheet">
<style>
  :root {
    --navy: #0c2747;
    --white: #ffffff;
    --ink: #2b2b2b;
    --field-border: #8a8f94;
    --btn-top: #4b8fdd;
    --btn-bottom: #2a5ea3;
    --olive: #74913a;
    --olive-border: #86a04c;
    --stat-bg: rgba(88, 98, 66, 0.62);
    --brand: #3f7fcf;
    --brand-dot: #f2c21b;
    --foliage-dark: #34501c;
    --foliage: #5d7f2c;
    --lake: #a7b26c;
    --grass: #6f9232;
    --warm: #d9c29a;
  }
  * { box-sizing: border-box; margin: 0; padding: 0; }
  html, body { width: 1200px; height: 737px; overflow: hidden; }
  body {
    position: relative;
    font-family: "Open Sans", sans-serif;
    background: var(--navy);
    color: var(--white);
  }
  .site-header {
    position: absolute; left: 0; top: 0; width: 1200px; height: 40px;
    background: var(--navy);
  }
  .brand {
    position: absolute; left: 262px; top: 6px;
    display: flex; align-items: center; gap: 7px;
    font-weight: 700; font-size: 19px; line-height: 24px; color: var(--brand);
  }
  .brand-dot { width: 13px; height: 13px; border-radius: 50%; background: var(--brand-dot); }

  .hero {
    position: absolute; left: 0; top: 40px; width: 1200px; height: 657px;
    overflow: hidden;
  }
  .hero-photo {
    position: absolute; inset: 0;
    background:
      radial-gradient(ellipse 230px 300px at 600px 360px, rgba(217,194,154,0.55), rgba(217,194,154,0) 72%),
      radial-gradient(ellipse 160px 330px at 700px 470px, rgba(168,176,60,0.55), rgba(168,176,60,0) 75%),
      radial-gradient(ellipse 300px 160px at 130px 120px, rgba(36,60,18,0.75), rgba(36,60,18,0) 75%),
      radial-gradient(ellipse 380px 170px at 1000px 90px, rgba(60,92,30,0.55), rgba(60,92,30,0) 75%),
      linear-gradient(180deg, var(--foliage-dark) 0%, var(--foliage) 28%, #7d9443 42%, var(--lake) 50%, #98ab5a 62%, var(--grass) 80%, #54772a 100%);
  }

  .stat-card {
    position: absolute; left: 148px; top: 77px; width: 178px; height: 179px;
    background: var(--stat-bg); border-radius: 10px;
    text-align: center; padding: 12px 14px 0;
  }
  .stat-value { font-weight: 300; font-size: 44px; line-height: 48px; }
  .stat-text { font-size: 13.5px; line-height: 18px; margin-top: 2px; }
  .stat-text strong { font-weight: 700; }

  .headline {
    position: absolute; right: 148px; top: 82px;
    text-align: right; font-weight: 300; font-size: 56px; line-height: 73px;
    letter-spacing: -0.5px;
    text-shadow: 1px 2px 4px rgba(0,0,0,0.35);
  }

  .lead-form { position: absolute; left: 828px; top: 316px; width: 230px; }
  .field {
    display: block; width: 230px; height: 34px; margin-bottom: 14px;
    border: 1px solid var(--field-border); border-radius: 5px; background: var(--white);
    font-family: inherit; font-size: 14px; color: var(--ink); padding: 0 10px;
  }
  .field::placeholder { color: var(--ink); }
  .cta {
    display: block; width: 230px; height: 63px; margin-top: 1px;
    border: 1px solid #3a6aa8; border-radius: 5px;
    background: linear-gradient(180deg, var(--btn-top), var(--btn-bottom));
    color: var(--white); font-family: inherit; font-size: 13.5px; line-height: 18px;
  }
  .cta-strong { font-size: 14.5px; }

  .offer {
    position: absolute; left: 828px; top: 538px; width: 199px; height: 68px;
    background: var(--olive); border: 1px solid var(--olive-border); border-radius: 5px;
    text-align: center; font-size: 13px; line-height: 17px; padding-top: 7px;
  }

  .site-footer {
    position: absolute; left: 0; top: 697px; width: 1200px; height: 40px;
    background: var(--navy);
  }
</style>
</head>
<body>
  <header class="site-header">
    <div class="brand"><span class="brand-dot"></span>Aerolume</div>
  </header>

  <main class="hero">
    <div class="hero-photo" role="img" aria-label="Photo of a woman in a green patterned top with arms spread wide, head tilted back breathing fresh air in a sunlit meadow beside a lake with trees behind"></div>

    <aside class="stat-card">
      <div class="stat-value">86%</div>
      <p class="stat-text">say their home became more <strong>efficient</strong> and more <strong>healthy</strong> after installing the Ductless HEAT and COOL System.</p>
    </aside>

    <h1 class="headline">How deep do<br>you want to<br>breathe?</h1>

    <form class="lead-form">
      <input class="field" type="text" placeholder="Type in your name">
      <input class="field" type="email" placeholder="e-mail address">
      <button class="cta" type="button">I want a <span class="cta-strong">FREE CONSULT</span><br>on heating and cooling a house.</button>
    </form>

    <div class="offer">$500 DISCOUNT<br>for ductless heat and cool<br>systems if you decide for one.</div>
  </main>

  <footer class="site-footer"></footer>
</body>
</html>
```